Brivane Communications - veteran and exclusive boutique copywriting agency

PROJECT NEEDS:
1. Website design - full homepage design and inner page top banner design
2. Logo design
* Please see attached Briefs (Word Docs) for descriptions of what is needed for 1 and 2 above.
ABOUT THE CLIENT:
Brivane Communications is a veteran and exclusive boutique copywriting agency run by Martin Olafsky. Martin is an award-winning published novelist and an accomplished executive ghostwriter with articles regularly published prominent technology publications like Pulsar, ByteHarbor, CapitalDrift, and more. For nearly three decades, Martin has focused solely on the technology sector - serving clients in Israel, Europe and the US.

Target Market(s)

hi-tech companies run by serious, confident professionals.

Industry/Entity Type

Business

Number of Pages Required

2 page

Font styles to use
Sans Serif
Other font styles liked:
• font should be modern

Colors
0054AA
0677BA
7BADD7
CADEEF
E8F1F8
F0912C
F2A743
F7CA91
FBE8D2
FDF5EE

Requirements
Must have
• psd files for logo, homepage design, and inner page top banner design
Nice to have
• Please see attached Website and Logo Design Briefs (Word Docs)
Should not have

```html
<!DOCTYPE html>
<html lang="en">
<head>
<meta charset="utf-8">
<title>Brivane Communications</title>
<link rel="stylesheet" href="https://fonts.googleapis.com/css2?family=Montserrat:wght@500;600;700;800&family=Barlow:wght@400;500;600&display=swap">
<style>
:root{
  --blue:#0054AA;
  --blue-mid:#0677BA;
  --blue-soft:#7BADD7;
  --blue-pale:#CADEEF;
  --blue-mist:#E8F1F8;
  --orange:#F0912C;
  --orange-warm:#F2A743;
  --orange-soft:#F7CA91;
  --grey-band:#F0F4F8;
  --ink:#2B2F36;
  --ink-soft:#4A4F57;
  --white:#fff;
  --head:'Montserrat',sans-serif;
  --body:'Barlow',sans-serif;
}
*{box-sizing:border-box;margin:0;padding:0}
html,body{width:1200px;height:3343px;overflow:hidden}
body{position:relative;background:var(--white);font-family:var(--body);color:var(--ink)}
.abs{position:absolute}
svg.abs{display:block}

/* header */
.brand{position:absolute;left:140px;top:14px;text-align:left}
.brand-name{font-family:var(--head);font-weight:800;font-size:38px;color:var(--blue);letter-spacing:1px;line-height:1}
.brand-sub{font-family:var(--head);font-weight:500;font-size:15px;color:var(--orange);letter-spacing:.5px;margin-top:4px}
.nav a{position:absolute;top:36px;font-family:var(--head);font-size:13px;font-weight:500;color:var(--blue-mid);letter-spacing:.6px;text-decoration:none}
.nav a.active{border-bottom:2px solid var(--blue-mid);padding-bottom:4px}
.nav a.on-blue{color:var(--white)}
.btn{position:absolute;display:flex;align-items:center;justify-content:center;font-family:var(--head);font-weight:700;color:var(--white);letter-spacing:.5px;text-decoration:none}
.btn-nav{left:978px;top:25px;width:137px;height:38px;background:var(--orange);font-size:13px;font-weight:600}

/* hero */
.hero-title{position:absolute;left:135px;top:215px;font-family:var(--head);font-size:60px;line-height:66px;font-weight:500;color:var(--blue)}
.hero-title strong{display:block;color:var(--orange);font-weight:800}
.hero-lead{position:absolute;left:140px;top:354px;width:420px;font-family:var(--head);font-size:18px;line-height:29px;color:var(--ink)}
.btn-hero{left:141px;top:432px;width:178px;height:48px;background:var(--blue);font-size:14px;overflow:hidden}
.btn-hero::after{content:"";position:absolute;right:-14px;bottom:-14px;width:30px;height:30px;border-radius:50%;background:var(--orange)}
.hero-photo{position:absolute;left:700px;top:80px;width:380px;height:576px;border-radius:190px 190px 0 0;background:linear-gradient(180deg,#9CC0E3 0%,#6E9CCB 55%,#2F4A6B 100%)}
.scroll-hint{position:absolute;left:1167px;top:260px;font-family:var(--head);font-size:11px;letter-spacing:3px;color:var(--blue-soft);writing-mode:vertical-rl}

/* client strip */
.clients{position:absolute;left:112px;top:656px;width:994px;height:116px;background:var(--white);box-shadow:0 8px 30px rgba(0,60,120,.12);border-radius:4px}
.clients span{position:absolute;top:42px;font-family:var(--head);font-weight:700;font-size:21px;color:var(--ink-soft)}
.clients .dot{display:inline-block;width:12px;height:12px;border-radius:50%;margin-right:7px;vertical-align:1px}
.clients .arrow{position:absolute;top:44px;font-family:var(--head);font-size:24px;color:var(--ink-soft);font-weight:500}

/* service cards */
.card{position:absolute;width:230px;background:var(--white);box-shadow:0 6px 24px rgba(0,40,90,.12);border-radius:6px;padding:22px 22px}
.card h3{font-family:var(--head);font-weight:700;font-size:14px;color:var(--blue);letter-spacing:.4px;margin-top:12px}
.card h4{font-family:var(--head);font-weight:700;font-size:10.5px;margin-top:12px;color:var(--ink)}
.card p{font-family:var(--head);font-size:9.6px;line-height:14px;margin-top:6px;color:var(--ink-soft)}
.card-blue{background:var(--blue)}
.card-blue h3,.card-blue h4{color:var(--white)}
.card-blue p{color:#DCE9F6}
.card svg{display:block}

/* what I do */
.section-title{position:absolute;font-family:var(--head);font-weight:600;color:var(--blue);letter-spacing:1px}
.copy{position:absolute;font-size:17.5px;line-height:29px;color:var(--ink-soft)}
.copy p+p{margin-top:14px}
.btn-pill{border-radius:24px;background:var(--orange)}
.kicker{position:absolute;font-family:var(--head);font-size:12px;font-weight:600;color:var(--orange);letter-spacing:.6px}

/* why choose */
.why-band{position:absolute;left:0;top:1343px;width:1200px;height:594px;background:var(--grey-band)}
.why-photo{position:absolute;left:753px;top:1402px;width:444px;height:444px;border-radius:50%;background:radial-gradient(circle at 50% 45%,#5a5a5a 0%,#2c2c2c 45%,#cfd4d8 80%)}

/* testimonial */
.quote-box{position:absolute;left:255px;top:2088px;width:698px;height:237px;background:var(--white);border:1px solid var(--blue-soft);border-radius:4px;text-align:center;padding:85px 40px 0}
.quote-box p{font-size:17.5px;line-height:27px;color:var(--ink)}
.quote-box cite{display:block;margin-top:15px;font-style:normal;font-weight:600;font-size:14px}
.slider-arrow{position:absolute;top:2180px}

/* contact */
.contact-band{position:absolute;left:0;top:2450px;width:1200px;height:563px;background:linear-gradient(135deg,#0A5BB5 0%,#0054AA 55%,#0049A0 100%)}
.contact-photo{position:absolute;left:130px;top:2510px;width:390px;height:503px;border-radius:160px 160px 0 0;background:linear-gradient(180deg,#6F7884 0%,#3A4049 50%,#1E2228 100%)}
.field{position:absolute;background:var(--white);font-size:14px;color:var(--ink-soft);padding:18px 20px}
.label-light{color:var(--white)}

/* footer */
.foot-col{position:absolute;top:3040px;height:240px;border-left:2px solid var(--blue-pale)}
.foot-col h5{position:absolute;left:20px;top:30px;font-family:var(--head);font-weight:700;font-size:14px;color:var(--blue);letter-spacing:1px;white-space:nowrap}
.foot-col ul{position:absolute;left:20px;top:64px;list-style:none;font-family:var(--head);font-size:12px;color:var(--ink);line-height:28px;white-space:nowrap}
.contact-line{display:flex;gap:12px;align-items:flex-start;line-height:16px;margin-bottom:18px}
.icon-round{flex:0 0 28px;height:28px;border-radius:50%;background:var(--blue);display:flex;align-items:center;justify-content:center}
.social{position:absolute;top:3154px;width:26px;height:26px;border-radius:50%;border:2px solid var(--blue)}
.copyright{position:absolute;left:0;top:3282px;width:1200px;border-top:1px solid var(--blue-pale);text-align:center;padding-top:24px;font-family:var(--head);font-size:12px;color:var(--ink)}
.copyright u{color:var(--blue)}
</style>
</head>
<body>

<!-- hero backdrop -->
<svg class="abs" style="left:0;top:0" width="1200" height="800" viewBox="0 0 1200 800">
  <path d="M736 0 C720 90 690 130 640 170 C585 215 560 320 575 420 C590 530 640 610 700 655 L1050 655 C1120 680 1170 730 1200 768 L1200 0 Z" fill="#0054AA"/>
</svg>
<div class="hero-photo" role="img" aria-label="Portrait photo of Martin Olafsky in a light blue shirt"></div>
<div class="scroll-hint">SCROLL DOWN</div>
<svg class="abs" style="left:1173px;top:412px" width="12" height="28" viewBox="0 0 12 28"><path d="M6 0 V26 M1 21 L6 27 L11 21" stroke="#F0912C" stroke-width="1.6" fill="none"/></svg>

<header>
  <div class="brand">
    <div class="brand-name">BRIVANE</div>
    <div class="brand-sub">Communications</div>
  </div>
  <nav class="nav">
    <a class="active" style="left:365px">ABOUT</a>
    <a style="left:470px">SERVICES</a>
    <a style="left:595px">INDUSTRIES</a>
    <a class="on-blue" style="left:733px">PORTFOLIO</a>
    <a class="on-blue" style="left:870px">CLIENTS</a>
  </nav>
  <a class="btn btn-nav">CONTACT ›</a>
</header>

<h1 class="hero-title">YOUR VOICE,<strong>MY WORDS.</strong></h1>
<p class="hero-lead">Copywriting and executive ghostwriting that speaks for your vision and your technology.</p>
<a class="btn btn-hero">CONTACT US ›</a>

<!-- orange blob behind services -->
<svg class="abs" style="left:0;top:680px" width="560" height="560" viewBox="0 0 560 560">
  <path d="M0 2 C80 -10 150 20 190 80 C230 140 320 160 420 170 C510 180 530 260 500 320 C470 380 420 420 390 500 C370 550 340 560 300 520 L0 400 Z" fill="#F0912C"/>
</svg>
<svg class="abs" style="left:1080px;top:700px" width="120" height="70" viewBox="0 0 120 70"><path d="M0 70 C30 20 80 0 120 40 L120 70 Z" fill="#0054AA"/></svg>

<div class="clients">
  <span class="arrow" style="left:30px">‹</span>
  <span style="left:70px"><i class="dot" style="background:#F0912C"></i>norvale</span>
  <span style="left:240px">tessaro</span>
  <span style="left:400px">quillon</span>
  <span style="left:540px">veridane</span>
  <span style="left:683px">halcyra</span>
  <span style="left:840px">ostrava</span>
  <span class="arrow" style="left:948px">›</span>
</div>

<!-- dotted accents -->
<svg class="abs" style="left:345px;top:920px" width="115" height="70"><defs><pattern id="dots" width="9" height="9" patternUnits="userSpaceOnUse"><circle cx="2" cy="2" r="1.2" fill="#F0912C"/></pattern></defs><rect width="115" height="70" fill="url(#dots)"/></svg>

<div class="card" style="left:112px;top:873px;height:200px">
  <svg width="48" height="48" viewBox="0 0 48 48" fill="none" stroke="#F0912C" stroke-width="1.8"><circle cx="24" cy="22" r="10"/><path d="M20 32 H28 M21 36 H27 M24 4 V8 M8 22 H4 M44 22 H40 M12 10 L9 7 M36 10 L39 7"/></svg>
  <h3>MESSAGING</h3>
  <h4>The Value of a Fresh Perspective</h4>
  <p>Could you be reaching farther? Clearly-defined, accurately-targeted messaging is crucial.</p>
</div>
<div class="card" style="left:112px;top:1088px;height:195px">
  <svg width="44" height="44" viewBox="0 0 44 44" fill="none" stroke="#F0912C" stroke-width="1.8"><rect x="6" y="4" width="22" height="34"/><rect x="20" y="14" width="18" height="24"/><path d="M10 10 H22 M10 16 H16 M24 22 H34 M24 28 H34"/></svg>
  <h3>COLLATERAL</h3>
  <h4>Concise, Effective, Creative</h4>
  <p>Marketing collateral that effectively communicates who you are and what you want to say.</p>
</div>
<div class="card card-blue" style="left:362px;top:980px;height:205px">
  <svg width="42" height="42" viewBox="0 0 42 42" fill="none" stroke="#fff" stroke-width="1.8"><rect x="4" y="4" width="30" height="34" rx="2"/><path d="M4 12 H34 M10 19 H28 M10 25 H28 M10 31 H22"/></svg>
  <h3>CONTENT MARKETING</h3>
  <h4>Giving Voice to Your Vision</h4>
  <p>Articles, blog content, white papers, e-books. Your ideas and expertise, our words.</p>
</div>

<h2 class="section-title" style="left:638px;top:915px;font-size:35px">WHAT I DO</h2>
<svg class="abs" style="left:965px;top:928px" width="235" height="20"><path d="M1 2 V18 M1 10 H235" stroke="#0677BA" stroke-width="1.5"/></svg>
<div class="copy" style="left:643px;top:975px;width:490px">
  <p>Based just north of Tel Aviv, Brivane Communications provides messaging, collateral creation, creative, content marketing, and consulting to companies in Israel and abroad.</p>
  <p>My writing is concise, elegant, and professional - while at the same time reflecting an understated creativity and sense of humor that brings company messages to a very intimate, personal level. I offer clients a deep understanding of business</p>
</div>
<a class="btn btn-pill" style="left:640px;top:1212px;width:152px;height:40px;font-size:12px">LEARN MORE</a>

<!-- why choose -->
<div class="why-band"></div>
<span class="kicker" style="left:136px;top:1452px">WHY WE ARE</span>
<svg class="abs" style="left:0;top:1482px" width="122" height="20"><path d="M0 10 H120 M120 2 V18" stroke="#0677BA" stroke-width="1.5"/></svg>
<h2 class="section-title" style="left:139px;top:1474px;font-size:31px">WHY CHOOSE ME</h2>
<div class="copy" style="left:140px;top:1522px;width:420px">
  <p>In a noisy marketplace, the value of clearly-defined, accurately-targeted, and well-conceived company messages is easy to see.</p>
  <p>However, what's clear to you may be less so to others. Are the messages and texts you've been recycling hitting their mark with all prospects? Could you be saying more? Could you be reaching farther?</p>
</div>
<a class="btn btn-pill" style="left:139px;top:1764px;width:173px;height:46px;font-size:13px">LEARN MORE ›</a>
<svg class="abs" style="left:720px;top:1366px" width="516" height="516" viewBox="0 0 516 516" fill="none" stroke="#7BADD7" stroke-width="1.2"><circle cx="258" cy="258" r="246"/><circle cx="258" cy="258" r="257"/><circle cx="258" cy="258" r="236"/></svg>
<div class="why-photo" role="img" aria-label="Photo of a desktop computer screen displaying the word copywriting"></div>

<!-- testimonials -->
<span class="kicker" style="left:0;width:1210px;text-align:center;top:1991px">TESTIMONIALS</span>
<h2 class="section-title" style="left:0;width:1210px;text-align:center;top:2004px;font-size:29px">WHAT THEY'RE SAYING</h2>
<svg class="abs" style="left:560px;top:2046px" width="80" height="4"><rect width="80" height="1.5" y="1" fill="#F7CA91"/><rect x="28" width="22" height="3" fill="#F0912C"/></svg>
<div class="abs" style="left:245px;top:2082px;width:165px;height:143px;background:var(--orange)"></div>
<div class="abs" style="left:800px;top:2185px;width:162px;height:140px;background:var(--blue)"></div>
<svg class="abs" style="left:885px;top:2245px" width="100" height="100"><defs><pattern id="dots2" width="9" height="9" patternUnits="userSpaceOnUse"><circle cx="2" cy="2" r="1.3" fill="#0054AA"/></pattern></defs><path d="M86 0 H100 V100 H0 V86 H86 Z" fill="url(#dots2)"/></svg>
<div class="quote-box">
  <svg class="abs" style="left:328px;top:26px" width="44" height="32" viewBox="0 0 44 32" fill="#0054AA"><path d="M18 4 C8 6 2 12 2 22 C2 28 6 31 10 31 C15 31 18 28 18 23 C18 18 15 15 10 15 C11 11 14 8 18 7 Z M42 4 C32 6 26 12 26 22 C26 28 30 31 34 31 C39 31 42 28 42 23 C42 18 39 15 34 15 C35 11 38 8 42 7 Z"/></svg>
  <p>“We've been working with Martin for over three years. He understands our technology and business model - and communicates it succinctly, in a language that our target audience understands and responds to.”</p>
  <cite>Eitan Marcovy, CTO, Ostrava Labs</cite>
</div>
<svg class="slider-arrow" style="left:130px" width="26" height="50" viewBox="0 0 26 50"><path d="M24 2 L3 25 L24 48" stroke="#0054AA" stroke-width="2.5" fill="none"/></svg>
<svg class="slider-arrow" style="left:1044px" width="26" height="50" viewBox="0 0 26 50"><path d="M2 2 L23 25 L2 48" stroke="#0054AA" stroke-width="2.5" fill="none"/></svg>

<!-- contact -->
<div class="contact-band"></div>
<div class="abs" style="left:83px;top:2568px;width:444px;height:444px;border-radius:50%;background:var(--orange-warm)"></div>
<div class="abs" style="left:0;top:2850px;width:83px;height:163px"></div>
<div class="contact-photo" role="img" aria-label="Photo of Martin Olafsky outdoors in a dark jacket and knit hat"></div>
<span class="kicker label-light" style="left:547px;top:2531px">GET IN TOUCH</span>
<h2 class="section-title label-light" style="left:546px;top:2550px;font-size:29px;color:#fff">CONTACT US NOW</h2>
<svg class="abs" style="left:547px;top:2591px" width="80" height="4"><rect width="80" height="1.5" y="1" fill="#7BADD7"/><rect x="28" width="22" height="3" fill="#fff"/></svg>
<div class="field" style="left:546px;top:2617px;width:269px;height:51px">First Name*</div>
<div class="field" style="left:823px;top:2617px;width:269px;height:51px">Last Name*</div>
<div class="field" style="left:546px;top:2678px;width:269px;height:51px">Email address*</div>
<div class="field" style="left:823px;top:2678px;width:269px;height:51px">Phone*</div>
<div class="field" style="left:546px;top:2739px;width:546px;height:109px;padding:14px 26px">Leave Message</div>
<a class="btn btn-pill" style="left:545px;top:2866px;width:203px;height:45px;font-size:14px">SEND MESSAGE</a>

<!-- footer -->
<footer>
  <div class="brand" style="left:165px;top:3066px">
    <div class="brand-name" style="font-size:42px">BRIVANE</div>
    <div class="brand-sub" style="font-size:16px;text-align:center">Communications</div>
  </div>
  <span class="social" style="left:166px" role="img" aria-label="Social profile"></span>
  <span class="social" style="left:201px" role="img" aria-label="Social profile"></span>
  <span class="social" style="left:236px" role="img" aria-label="Social profile"></span>
  <span class="social" style="left:271px" role="img" aria-label="Social profile"></span>

  <div class="foot-col" style="left:410px;width:200px">
    <h5 style="border-left:2px solid var(--blue);left:0;padding-left:20px">NAVIGATION</h5>
    <ul><li>About</li><li>Services</li><li>Industries</li><li>Portfolio</li><li>Clients</li></ul>
  </div>
  <div class="foot-col" style="left:610px;width:216px">
    <h5 style="border-left:2px solid var(--blue);left:0;padding-left:20px">RESOURCES</h5>
    <ul><li>Privacy Policy</li><li>Terms of Use</li><li>Sitemap</li><li>Contact Us</li></ul>
  </div>
  <div class="foot-col" style="left:826px;width:300px">
    <h5 style="border-left:2px solid var(--blue);left:0;padding-left:20px">CONTACT US</h5>
    <ul style="line-height:16px;top:68px">
      <li class="contact-line"><span class="icon-round"><svg width="12" height="14" viewBox="0 0 12 14"><path d="M6 0 C2.7 0 0 2.5 0 5.6 C0 9.5 6 14 6 14 C6 14 12 9.5 12 5.6 C12 2.5 9.3 0 6 0 Z" fill="#fff"/><circle cx="6" cy="5.6" r="2" fill="#0054AA"/></svg></span><span>P.O. Box 5127<br>Neveh Arbel, Israel 40811</span></li>
      <li class="contact-line"><span class="icon-round"><svg width="13" height="13" viewBox="0 0 13 13"><path d="M2.6 0.5 L4.6 3.2 L3.4 4.8 C4.2 6.6 6.4 8.8 8.2 9.6 L9.8 8.4 L12.5 10.4 L11 12.5 C5.5 12.5 0.5 7.5 0.5 2 Z" fill="#fff"/></svg></span><span style="padding-top:6px">+972-50-618-2097</span></li>
      <li class="contact-line"><span class="icon-round"><svg width="14" height="10" viewBox="0 0 14 10"><rect x="0.5" y="0.5" width="13" height="9" fill="#fff"/><path d="M0.5 0.5 L7 5.5 L13.5 0.5" stroke="#0054AA" fill="none"/></svg></span><span style="padding-top:6px">hello@brivane.co.il</span></li>
    </ul>
  </div>
  <div class="copyright">Copyright © 2023 <u>Brivane Communications.</u> All Right Reserved</div>
</footer>

</body>
</html>
```